Tovex - Business Card Design

Design a modern masculine business card for our business

Target Market(s)

Private Market

Industry/Entity Type

Construction

Contact Information for Business Card

Company Name - Name of Person - Address - email address - contact number

Font styles to use
Serif
Sans Serif

Colors
0094D4
00A9DD
6FCCEA
C7EBF8
E9F6FB
00AB8E
00BBA5
67D7C9
C6EFE9
E9F9F6
F0912C
F2A743
F7CA91
FBE8D2
FDF5EE

Requirements
Must have
• Use company logo provided
Nice to have
• Company Logo

```html
<!DOCTYPE html>
<html lang="en">
<head>
<meta charset="utf-8">
<title>Tovex – Business Card</title>
<link rel="stylesheet" href="https://fonts.googleapis.com/css2?family=Krona+One&family=Roboto:wght@400&display=swap">
<style>
  :root {
    --stage: #e8e8ec;
    --paper: #ffffff;
    --ink: #000000;
    --accent: #f4722e;
    --light-text: #ffffff;
  }
  * { margin: 0; padding: 0; box-sizing: border-box; }
  html, body { width: 1200px; height: 1200px; overflow: hidden; }
  body { background: var(--stage); position: relative; font-family: "Roboto", sans-serif; }

  .card {
    position: absolute;
    left: 277px;
    width: 649px;
    height: 418px;
    overflow: hidden;
  }
  .card--front { top: 156px; background: var(--paper); }
  .card--back { top: 629px; background: var(--ink); }

  .card__band { position: absolute; left: 0; top: 0; width: 649px; height: 418px; }

  .wordmark {
    position: absolute;
    display: flex;
    align-items: center;
    gap: 10px;
    font-family: "Krona One", sans-serif;
    font-weight: 400;
    line-height: 1;
    white-space: nowrap;
  }
  .wordmark__square { width: 14px; height: 14px; background: var(--accent); flex: none; }
  .wordmark__text { display: flex; flex-direction: column; gap: 6px; }
  .wordmark__name { font-size: 40px; letter-spacing: 1px; }
  .wordmark__sub { font-size: 9.5px; letter-spacing: 1.2px; }

  .card--front .wordmark { left: 70px; top: 140px; color: var(--ink); }
  .card--back .wordmark { left: 190px; top: 175px; color: var(--light-text); }
  .card--back .wordmark__square { width: 18px; height: 18px; }
  .card--back .wordmark__name { font-size: 52px; }
  .card--back .wordmark__sub { font-size: 12px; }

  .person-name {
    position: absolute;
    left: 347px;
    top: 134px;
    font-family: "Krona One", sans-serif;
    font-size: 29px;
    color: var(--ink);
    letter-spacing: -0.5px;
  }

  .contact-list { position: absolute; left: 345px; top: 204px; list-style: none; }
  .contact-list li {
    display: flex;
    align-items: center;
    gap: 8px;
    height: 20px;
    margin-bottom: 9px;
    font-size: 16px;
    color: var(--ink);
  }
  .icon { width: 20px; height: 20px; flex: none; display: block; }

  .address {
    position: absolute;
    left: 345px;
    top: 319px;
    display: flex;
    align-items: center;
    gap: 8px;
    font-size: 16px;
    color: var(--light-text);
  }
</style>
</head>
<body>

<section class="card card--front" aria-label="Business card front">
  <svg class="card__band" viewBox="0 0 973 627" aria-hidden="true">
    <polygon fill="var(--accent)" points="0,457 35,457 83,531 0,531"/>
    <polygon fill="var(--accent)" points="52,457 125,457 175,531 101,531"/>
    <polygon fill="var(--accent)" points="142,457 215,457 265,531 191,531"/>
    <polygon fill="var(--accent)" points="232,457 305,457 355,531 281,531"/>
    <polygon fill="var(--accent)" points="322,457 395,457 446,531 373,531"/>
    <polygon fill="var(--ink)" points="432,457 973,457 973,531 484,531"/>
  </svg>

  <div class="wordmark">
    <span class="wordmark__square"></span>
    <span class="wordmark__text">
      <span class="wordmark__name">TOVEX</span>
      <span class="wordmark__sub">CONSTRUCTION, INC</span>
    </span>
  </div>

  <h1 class="person-name">yourname</h1>

  <ul class="contact-list">
    <li>
      <svg class="icon" viewBox="0 0 20 20" aria-hidden="true">
        <rect width="20" height="20" rx="3" fill="var(--accent)"/>
        <path d="M6.5 4.5l2 2.5-1.2 1.3c.7 1.6 1.9 2.8 3.4 3.5l1.3-1.2 2.5 2-1.3 1.9C9.6 14.3 5.8 10.5 5 6.3z" fill="#fff"/>
      </svg>
      123 456 789
    </li>
    <li>
      <svg class="icon" viewBox="0 0 20 20" aria-hidden="true">
        <rect width="20" height="20" rx="3" fill="var(--accent)"/>
        <g fill="none" stroke="#fff" stroke-width="1">
          <circle cx="10" cy="10" r="5.5"/>
          <ellipse cx="10" cy="10" rx="2.4" ry="5.5"/>
          <path d="M4.5 10h11M5.3 7.2h9.4M5.3 12.8h9.4"/>
        </g>
      </svg>
      www.yourname.com
    </li>
    <li>
      <svg class="icon" viewBox="0 0 20 20" aria-hidden="true">
        <rect width="20" height="20" rx="3" fill="var(--accent)"/>
        <rect x="5" y="6.5" width="10" height="7" fill="none" stroke="#fff" stroke-width="1"/>
        <path d="M5 6.5l5 4 5-4" fill="none" stroke="#fff" stroke-width="1"/>
      </svg>
      yourname@mailbox.com
    </li>
  </ul>

  <p class="address">
    <svg class="icon" viewBox="0 0 20 20" aria-hidden="true">
      <rect width="20" height="20" rx="3" fill="#fff"/>
      <path d="M10 4.5a3.5 3.5 0 0 0-3.5 3.5c0 2.6 3.5 7 3.5 7s3.5-4.4 3.5-7A3.5 3.5 0 0 0 10 4.5z" fill="var(--accent)"/>
      <circle cx="10" cy="8" r="1.3" fill="#fff"/>
    </svg>
    2750 N Ridgeline Pkwy, Ste 140
  </p>
</section>

<section class="card card--back" aria-label="Business card back">
  <div class="wordmark">
    <span class="wordmark__square"></span>
    <span class="wordmark__text">
      <span class="wordmark__name">TOVEX</span>
      <span class="wordmark__sub">CONSTRUCTION, INC</span>
    </span>
  </div>
</section>

</body>
</html>
```